Brimovex business card

Based on company logo and website given , to design a business card temple. Slogan "Your furry friends deserves the best"
Color style please refer to our website

```html
<!DOCTYPE html>
<html lang="en">
<head>
<meta charset="utf-8">
<title>Brimovex business card</title>
<link rel="stylesheet" href="https://fonts.googleapis.com/css2?family=Lexend:wght@300;400;600&family=Noto+Serif:wght@400&display=swap">
<style>
  :root {
    --stage: #d6d6d6;
    --paper: #e6e4de;
    --forest: #1d5a36;
    --ink: #2b2b2b;
    --olive: #a29a1c;
    --photo-top: #3a4740;
    --photo-mid: #52504a;
    --photo-low: #7a5a3e;
    --cream: #ece8df;
  }
  * { box-sizing: border-box; margin: 0; padding: 0; }
  html, body { width: 1200px; height: 800px; overflow: hidden; }
  body {
    background: var(--stage);
    font-family: "Lexend", sans-serif;
    display: flex;
    align-items: center;
    justify-content: center;
    gap: 40px;
  }
  .card {
    position: relative;
    width: 520px;
    height: 320px;
    overflow: hidden;
  }

  /* Front side */
  .card-front { background: var(--paper); color: var(--ink); }
  .front-body { position: absolute; left: 40px; top: 46px; }
  .person-name {
    color: var(--forest);
    font-weight: 600;
    font-size: 24px;
    letter-spacing: 0.3px;
  }
  .person-role { font-weight: 300; font-size: 16px; margin-top: 6px; }
  .divider {
    width: 80px;
    border-top: 3px dotted var(--forest);
    margin: 24px 0 30px;
  }
  .contact-row { display: flex; font-size: 16px; font-weight: 300; line-height: 24px; }
  .contact-label { width: 70px; color: var(--forest); font-weight: 600; }
  .address { font-size: 16px; font-weight: 300; line-height: 24px; margin-top: 10px; }
  .website { font-size: 16px; font-weight: 300; margin-top: 12px; }
  .website strong { font-weight: 600; color: var(--forest); }
  .front-brand {
    position: absolute;
    right: 28px;
    top: 58px;
    display: flex;
    align-items: center;
    gap: 8px;
  }
  .brand-dot { width: 12px; height: 12px; border-radius: 50%; background: var(--olive); }
  .brand-name { color: var(--olive); font-weight: 400; font-size: 34px; letter-spacing: -0.5px; }
  .base-band {
    position: absolute;
    left: 0; right: 0; bottom: 0;
    height: 14px;
    background: var(--forest);
  }

  /* Back side */
  .card-back { background: var(--photo-top); }
  .back-photo {
    position: absolute; inset: 0;
    background:
      linear-gradient(160deg, var(--photo-top) 0%, #404843 40%, var(--photo-mid) 65%, var(--photo-low) 100%);
  }
  .back-brand {
    position: absolute;
    right: 40px;
    top: 92px;
    display: flex;
    align-items: center;
    gap: 10px;
  }
  .back-brand .brand-name { font-size: 54px; }
  .back-brand .brand-dot { width: 16px; height: 16px; }
  .slogan {
    position: absolute;
    right: 40px;
    top: 172px;
    color: var(--cream);
    font-family: "Noto Serif", serif;
    font-size: 17px;
    line-height: 22px;
    text-align: right;
  }
</style>
</head>
<body>
  <section class="card card-front">
    <div class="front-body">
      <h1 class="person-name">DANIEL FORSYTH</h1>
      <p class="person-role">Founder &amp; CEO</p>
      <div class="divider"></div>
      <div class="contact-row"><span class="contact-label">phone</span><span>+61 3 9000 4821</span></div>
      <div class="contact-row"><span class="contact-label">email</span><span>sales@brimovex.com.au</span></div>
      <p class="address">4/22 Harlow Street<br>Glen Ashby Vic 3152</p>
      <p class="website">www.<strong>brimovex</strong>.com.au</p>
    </div>
    <div class="front-brand">
      <span class="brand-dot"></span>
      <span class="brand-name">Brimovex</span>
    </div>
    <div class="base-band"></div>
  </section>

  <section class="card card-back">
    <div class="back-photo" role="img" aria-label="Photo of a person and a dog sitting on a grassy hillside looking out over a misty valley"></div>
    <div class="back-brand">
      <span class="brand-dot"></span>
      <span class="brand-name">Brimovex</span>
    </div>
    <p class="slogan">Your furry friends<br>deserves the best.</p>
  </section>
</body>
</html>
```